Stationery Design needed for logo design project

This project is linked to Professional LED lighting company needs a logo.

Our company needs a Stationery Design. Please refer to our original project in the link above.

```html
<!DOCTYPE html>
<html lang="en">
<head>
<meta charset="utf-8">
<title>Letterhead</title>
<link rel="stylesheet" href="https://fonts.googleapis.com/css2?family=Montserrat:wght@500;600&display=swap">
<style>
  :root {
    --brand-blue: #3333ff;
    --accent-red: #e60000;
    --blush: #fadbe4;
    --paper: #ffffff;
    --ink: #111111;
    --on-red: #ffffff;
  }
  html, body {
    margin: 0;
    padding: 0;
    width: 900px;
    height: 1200px;
    overflow: hidden;
    background: var(--paper);
  }
  .letterhead {
    position: relative;
    width: 900px;
    height: 1200px;
    background: var(--paper);
    font-family: "Montserrat", Arial, sans-serif;
    color: var(--ink);
    overflow: hidden;
  }
  .side-band {
    position: absolute;
    top: 0;
    height: 1200px;
    background: var(--brand-blue);
  }
  .side-band--left { left: 0; width: 64px; }
  .side-band--right { right: 0; width: 68px; }

  .sheet-backdrop {
    position: absolute;
    left: 64px;
    top: 0;
    width: 768px;
    height: 1200px;
  }

  .brand {
    position: absolute;
    left: 84px;
    top: 30px;
  }
  .brand__mark {
    position: absolute;
    left: 46px;
    top: 0;
    width: 114px;
    height: 94px;
    background: var(--brand-blue);
  }
  .brand__name {
    position: absolute;
    left: 0;
    top: 94px;
    margin: 0;
    font-size: 31px;
    font-weight: 500;
    white-space: nowrap;
  }

  .address {
    position: absolute;
    right: 90px;
    top: 72px;
    margin: 0;
    font-style: normal;
    font-size: 31px;
    font-weight: 500;
    line-height: 48px;
    text-align: right;
  }

  .header-rule {
    position: absolute;
    left: 64px;
    top: 176px;
    width: 768px;
    height: 4px;
    background: var(--brand-blue);
  }

  .memo-field {
    position: absolute;
    top: 182px;
    margin: 0;
    font-size: 25px;
    font-weight: 600;
  }
  .memo-field--number { left: 84px; }
  .memo-field--date { left: 556px; }

  .contact-footer {
    position: absolute;
    left: 64px;
    top: 1040px;
    width: 768px;
    height: 160px;
    background: var(--accent-red);
    color: var(--on-red);
    font-size: 26px;
    font-weight: 500;
  }
  .contact-footer__line {
    position: absolute;
    margin: 0;
    white-space: nowrap;
  }
  .contact-footer__phone { left: 20px; top: 16px; }
  .contact-footer__fax { left: 452px; top: 16px; }
  .contact-footer__email { left: 20px; top: 52px; }
  .contact-footer__web { left: 20px; top: 90px; }
</style>
</head>
<body>
<main class="letterhead">
  <svg class="sheet-backdrop" viewBox="0 0 768 1200" aria-hidden="true">
    <polygon points="768,184 768,1040 6,1040" fill="var(--blush)"/>
  </svg>

  <div class="side-band side-band--left"></div>
  <div class="side-band side-band--right"></div>

  <div class="brand">
    <div class="brand__mark"></div>
    <p class="brand__name">Company name</p>
  </div>

  <address class="address">
    House no-12, Lake View Road<br>
    Dhanmondi, Dhaka
  </address>

  <div class="header-rule"></div>

  <p class="memo-field memo-field--number">Memo no:</p>
  <p class="memo-field memo-field--date">Date:</p>

  <footer class="contact-footer">
    <p class="contact-footer__line contact-footer__phone">Phone: +880 51207, +880 51208</p>
    <p class="contact-footer__line contact-footer__fax">Fax: +880 51209</p>
    <p class="contact-footer__line contact-footer__email">Email: mail@lumacraft.com</p>
    <p class="contact-footer__line contact-footer__web">Web: www.lumacraft.com</p>
  </footer>
</main>
</body>
</html>
```